Services Brochure

We need an revised brochure for our 3 main services. I have uploaded our old Brochure for reference. We have 3 main services (Managed IT Services, Business VoIP, Business Internet). Below is some text we would like included in the brochure for each service section. In addition I have attached a "mock up" showing that we want IT Services on top, VoIP in the middle and Internet at the bottom. Please use your design experience to select images that would fit well. I also included an image of the phone we would like to use.
Text for Brochure:
Title/Header: Unleash the Power of Local IT Solutions
IT Services That Mean Business
Experience fanatical customer service with our affordable, full-service IT solutions. We’re 100% local, ensuring leading response times and personalized support—so you can focus on what you do best.
Talk More, Worry Less with Our Telephone Services
Say goodbye to overpriced equipment and hello to our free phone plan. Keep your number and enjoy unlimited local and long-distance calling. Tailor your phone system to your business needs and rest assured—our rates are always the lowest in town.
Highspeed Internet That Sets You Apart
Stay connected with blazing-fast speeds—from 1Gbps to 10Gbps, both up and down. Benefit from a static IP address and unbeatable prices, backed by 100% local support. Get the connectivity your business deserves at the best value in town.
Elevate your business with cutting-edge technology.
Sorry everyone the banner size is 81" high and 33" wide.

```html
<!DOCTYPE html>
<html lang="en">
<head>
<meta charset="utf-8">
<title>Nordbyte – Local IT Solutions Banner</title>
<link rel="stylesheet" href="https://fonts.googleapis.com/css2?family=Poppins:ital,wght@0,700;0,800;1,800&family=Outfit:wght@400&display=swap">
<style>
  :root {
    --stage: #6e6e6e;
    --paper: #ffffff;
    --brand-blue: #2b2f82;
    --brand-gray: #7d7d7d;
    --bar-gray: #8a8a8a;
    --card-gray: #ececed;
    --label-dark: #111114;
    --body-text: #505055;
    --footer-dark: #23232d;
  }
  * { margin: 0; padding: 0; box-sizing: border-box; }
  html, body { width: 1200px; height: 2432px; overflow: hidden; background: var(--stage); }
  .banner {
    position: absolute; left: 164px; top: 120px; width: 901px; height: 2210px;
    background: var(--paper); overflow: hidden;
  }
  .top-bar { position: absolute; left: 0; top: 0; width: 901px; height: 30px; }
  .hero {
    position: absolute; left: 0; top: 30px; width: 901px; height: 905px;
    background: radial-gradient(ellipse at 70% 35%, #e4e4e6 0%, #f0f0f2 45%, #f6f6f7 100%);
  }
  .brand-name {
    position: absolute; left: 0; top: 300px; width: 901px; text-align: center;
    font-family: "Poppins", sans-serif; font-weight: 800; font-size: 118px;
    line-height: 1; color: var(--brand-blue); letter-spacing: -3px;
  }
  .headline {
    position: absolute; left: 0; top: 628px; width: 901px; text-align: center;
    font-family: "Poppins", sans-serif; font-weight: 800; font-size: 85px;
    line-height: 79px; color: var(--brand-blue); letter-spacing: -1px;
  }
  .headline .accent { color: var(--brand-gray); }
  .service {
    position: absolute; top: 935px; width: 262px; height: 1025px;
    background: var(--card-gray);
    border-top-right-radius: 66px; border-bottom-left-radius: 56px;
    overflow: hidden;
  }
  .service--it { left: 43px; }
  .service--voip { left: 322px; }
  .service--internet { left: 600px; }
  .service__photo { height: 257px; }
  .service--it .service__photo { background: linear-gradient(135deg, #3a4654 0%, #7f8c96 45%, #c9ccd0 100%); }
  .service--voip .service__photo { background: linear-gradient(135deg, #2a2a2c 0%, #8a8b8d 50%, #d6d4d0 100%); }
  .service--internet .service__photo { background: linear-gradient(135deg, #3d3533 0%, #8f8582 50%, #bdb7b3 100%); }
  .service__label {
    height: 85px; background: var(--label-dark); color: #fff;
    display: flex; align-items: center; justify-content: center; text-align: center;
    font-family: "Poppins", sans-serif; font-weight: 800; font-size: 30px; line-height: 31px;
  }
  .service__text {
    padding: 26px 6px 0 36px;
    font-family: "Outfit", sans-serif; font-weight: 400; font-size: 27px; line-height: 32.5px;
    color: var(--body-text); white-space: nowrap;
  }
  .tagline {
    position: absolute; left: 0; top: 1984px; width: 901px; text-align: center;
    font-family: "Poppins", sans-serif; font-style: italic; font-weight: 800;
    color: var(--brand-blue); letter-spacing: -0.5px;
  }
  .tagline__lead { display: block; font-size: 29px; line-height: 38px; }
  .tagline__main { display: block; font-size: 46px; line-height: 52px; }
  .footer { position: absolute; left: 0; top: 2130px; width: 901px; height: 80px; }
  .footer__bg { position: absolute; left: 0; top: 0; }
  .contact {
    position: absolute; display: flex; align-items: center; gap: 8px; color: #fff;
    font-family: "Poppins", sans-serif; font-weight: 700; white-space: nowrap;
  }
  .contact svg { flex: none; display: block; }
  .contact--email { left: 32px; top: 9px; height: 71px; font-size: 19px; }
  .contact--phone { left: 288px; width: 336px; top: 0; height: 80px; justify-content: center; font-size: 34px; letter-spacing: 1px; }
  .contact--web { right: 28px; top: 9px; height: 71px; font-size: 19px; }
</style>
</head>
<body>
<main class="banner">
  <svg class="top-bar" width="901" height="30" viewBox="0 0 901 30" aria-hidden="true">
    <rect x="0" y="0" width="901" height="30" fill="var(--bar-gray)"/>
    <polygon points="0,0 478,0 458,30 0,30" fill="var(--brand-blue)"/>
    <polygon points="478,0 490,0 470,30 458,30" fill="#ffffff"/>
  </svg>

  <div class="hero" role="img" aria-label="Soft grey background of interlocking gears, a dotted wave and a hand reaching toward the name"></div>

  <div class="brand-name">Nordbyte</div>

  <h1 class="headline">UNLEASH THE<br>POWER OF LOCAL<br><span class="accent">IT SOLUTIONS</span></h1>

  <section class="service service--it">
    <div class="service__photo" role="img" aria-label="Support staff wearing headsets working at computers in a bright office"></div>
    <h2 class="service__label">MANAGED<br>IT SERVICES</h2>
    <p class="service__text">Experience<br>fanatical<br>customer<br>service with our<br>affordable,<br>full-service IT<br>solutions. We’re<br>100% local,<br>ensuring leading<br>response times<br>and<br>personalized<br>support—so you<br>can focus on<br>what you do<br>best.</p>
  </section>

  <section class="service service--voip">
    <div class="service__photo" role="img" aria-label="Hand dialing a desk IP telephone with the handset lifted"></div>
    <h2 class="service__label">BUSINESS<br>VOIP</h2>
    <p class="service__text">Say goodbye to<br>overpriced<br>equipment and<br>hello to our free<br>phone plan.<br>Keep your<br>number and<br>enjoy unlimited<br>local and<br>long-distance<br>calling. Tailor<br>your phone<br>system to your<br>business needs<br>and rest<br>assured—our<br>rates are always<br>the lowest in<br>town.</p>
  </section>

  <section class="service service--internet">
    <div class="service__photo" role="img" aria-label="Hands typing on a laptop with a glowing wifi symbol and login fields"></div>
    <h2 class="service__label">BUSINESS<br>INTERNET</h2>
    <p class="service__text">Stay connected<br>with<br>blazing-fast<br>speeds—from<br>1Gbps to<br>10Gbps, both up<br>and down.<br>Benefit from a<br>static IP address<br>and unbeatable<br>prices, backed<br>by 100% local<br>support. Get the<br>connectivity<br>your business<br>deserves at the<br>best value in<br>town.</p>
  </section>

  <p class="tagline">
    <span class="tagline__lead">Elevate your business with</span>
    <span class="tagline__main">cutting-edge technology</span>
  </p>

  <footer class="footer">
    <svg class="footer__bg" width="901" height="80" viewBox="0 0 901 80" aria-hidden="true">
      <rect x="0" y="9" width="901" height="71" fill="var(--footer-dark)"/>
      <polygon points="242,0 670,0 624,80 288,80" fill="var(--brand-blue)"/>
    </svg>
    <div class="contact contact--email">
      <svg width="22" height="16" viewBox="0 0 22 16" aria-hidden="true"><rect x="1" y="1" width="20" height="14" fill="none" stroke="#fff" stroke-width="1.6"/><polyline points="1,1 11,9 21,1" fill="none" stroke="#fff" stroke-width="1.6"/><line x1="1" y1="15" x2="8.5" y2="7" stroke="#fff" stroke-width="1.4"/><line x1="21" y1="15" x2="13.5" y2="7" stroke="#fff" stroke-width="1.4"/></svg>
      <span>sales@nordbyte.com</span>
    </div>
    <div class="contact contact--phone">
      <svg width="24" height="30" viewBox="0 0 24 30" aria-hidden="true"><path d="M6 2 L10 9 L7 12 C8 17 11 21 15 24 L18 21 L23 26 L19 29 C10 27 3 18 2 6 Z" fill="#fff"/></svg>
      <span>555-014-2287</span>
    </div>
    <div class="contact contact--web">
      <svg width="20" height="20" viewBox="0 0 20 20" aria-hidden="true"><g fill="none" stroke="#fff" stroke-width="1.4"><circle cx="10" cy="10" r="8.5"/><ellipse cx="10" cy="10" rx="4" ry="8.5"/><line x1="1.5" y1="10" x2="18.5" y2="10"/><line x1="3" y1="5.5" x2="17" y2="5.5"/><line x1="3" y1="14.5" x2="17" y2="14.5"/></g></svg>
      <span>www.nordbyte.com</span>
    </div>
  </footer>
</main>
</body>
</html>
```